Presentation Folder with inside Pockets

We need a Presentation Folder with inside pockets. The size of the folder will be 9" x 12" and will be printed on the cover, the back and the inside folder flaps. The design will be very simple and consist of our logo (large) on the front cover and our logo (smaller) and contact information on the back. We are open to various colors that you think may go along with our logo. When you display your work, show the front, back and inside.

Target Market(s)

Pharmaceutical Companies

Industry/Entity Type

Work

Requirements
Should not have
• please do not add stock medical photos.

```html
<!DOCTYPE html>
<html lang="en">
<head>
<meta charset="utf-8">
<title>Meridian Trials Inc. – Presentation Folder</title>
<link rel="stylesheet" href="https://fonts.googleapis.com/css2?family=Open+Sans:wght@400;600;700&display=swap">
<style>
  :root {
    --stage: #000000;
    --ink: #111111;
    --white: #ffffff;
    --grey-text: #444444;
    --mark: #6fb43a;
    --card-edge: #cfcfcf;
  }
  html, body {
    margin: 0;
    padding: 0;
    width: 1200px;
    height: 974px;
    overflow: hidden;
    background: var(--stage);
  }
  .folder {
    position: relative;
    width: 1200px;
    height: 974px;
    font-family: "Open Sans", Arial, sans-serif;
  }
  .folder-shapes {
    position: absolute;
    inset: 0;
  }
  .brand-name {
    margin: 0;
    font-family: "Open Sans", Arial, sans-serif;
    font-weight: 700;
    white-space: nowrap;
  }

  /* Back cover */
  .back-brand {
    position: absolute;
    left: 105px;
    top: 580px;
    width: 507px;
    text-align: center;
    color: var(--white);
    font-size: 28px;
    line-height: 36px;
  }
  .back-contact {
    position: absolute;
    left: 105px;
    top: 657px;
    width: 507px;
    text-align: center;
    color: var(--white);
    font-size: 12px;
    line-height: 22px;
  }
  .back-contact .contact-line { display: flex; justify-content: center; align-items: center; gap: 6px; }
  .back-contact svg { width: 12px; height: 12px; }
  .back-contact .gap { width: 6px; }

  /* Front cover */
  .front-brand {
    position: absolute;
    left: 672px;
    top: 162px;
    display: flex;
    align-items: center;
    gap: 14px;
    color: var(--ink);
  }
  .front-brand .brand-mark {
    width: 68px;
    height: 68px;
    border-radius: 50%;
    background: var(--mark);
  }
  .front-brand .brand-name { font-size: 28px; line-height: 36px; }
  .front-web {
    position: absolute;
    left: 700px;
    top: 681px;
    width: 376px;
    text-align: center;
    font-size: 12px;
    letter-spacing: 2.6px;
    color: var(--grey-text);
  }
  .front-web strong { font-weight: 700; }

  /* Business cards */
  .card {
    position: absolute;
    width: 196px;
    height: 112px;
    background: var(--white);
    box-shadow: 0 0 0 1px var(--card-edge);
    box-sizing: border-box;
    padding: 13px 10px 0 11px;
    color: var(--ink);
    font-size: 5px;
    line-height: 8px;
  }
  .card-left { left: 237px; top: 776px; }
  .card-right { left: 786px; top: 776px; }
  .card-brand { display: flex; align-items: center; gap: 5px; }
  .card-brand .brand-mark { width: 20px; height: 20px; border-radius: 50%; background: var(--mark); }
  .card-brand .brand-name { font-size: 8px; line-height: 10px; }
  .card-details { margin-top: 18px; display: flex; justify-content: space-between; }
  .card-person { text-align: center; font-weight: 600; font-size: 5.5px; line-height: 8px; margin-right: 22px; margin-top: 2px; color: var(--ink); }
  .card-address { margin-top: 9px; }
</style>
</head>
<body>
<div class="folder">
  <svg class="folder-shapes" width="1200" height="974" viewBox="0 0 1200 974" aria-hidden="true">
    <defs>
      <linearGradient id="back-cover-fill" x1="0" y1="0" x2="1" y2="0">
        <stop offset="0" stop-color="#1b93d3"/>
        <stop offset="1" stop-color="#0f4772"/>
      </linearGradient>
      <radialGradient id="green-fill" cx="0.5" cy="0.4" r="0.7">
        <stop offset="0" stop-color="#a3cc3c"/>
        <stop offset="1" stop-color="#5e9a35"/>
      </radialGradient>
      <radialGradient id="wave-fill" cx="0.4" cy="0.5" r="0.8">
        <stop offset="0" stop-color="#a5cf3a"/>
        <stop offset="1" stop-color="#5f9b36"/>
      </radialGradient>
      <radialGradient id="grey-fill" cx="0.5" cy="0.4" r="0.7">
        <stop offset="0" stop-color="#f8f8f8"/>
        <stop offset="1" stop-color="#d2d2d2"/>
      </radialGradient>
      <linearGradient id="rule-fill" x1="0" y1="0" x2="1" y2="0">
        <stop offset="0" stop-color="#ffffff" stop-opacity="0"/>
        <stop offset="0.5" stop-color="#ffffff" stop-opacity="0.45"/>
        <stop offset="1" stop-color="#ffffff" stop-opacity="0"/>
      </linearGradient>
    </defs>

    <!-- back cover -->
    <rect x="105" y="38" width="507" height="676" fill="url(#back-cover-fill)"/>
    <circle cx="352" cy="336" r="190" fill="#5b8aa6" opacity="0.35"/>
    <rect x="150" y="637" width="395" height="2" fill="url(#rule-fill)"/>

    <!-- front cover -->
    <rect x="612" y="38" width="506" height="676" fill="#ffffff"/>
    <path d="M612 38 H672 C645 110 636 220 666 330 C694 430 704 560 688 714 H612 Z" fill="url(#wave-fill)"/>
    <path d="M681 38 C652 110 644 220 674 330 C702 430 712 560 696 714" fill="none" stroke="#1670b4" stroke-width="3"/>

    <!-- left pocket -->
    <path d="M105 714 H608 L600 728 Q592 740 592 760 V910 Q592 940 570 940 H80 Q62 940 62 922 V730 Q62 722 72 721 Z" fill="url(#grey-fill)"/>
    <!-- right pocket -->
    <path d="M614 714 H1118 L1154 724 Q1163 727 1163 736 V926 Q1163 940 1148 940 H658 Q636 940 634 918 L630 740 Q628 724 614 714 Z" fill="url(#green-fill)"/>

    <!-- card slots -->
    <g stroke="#bfbfbf" stroke-width="1">
      <line x1="230" y1="785" x2="256" y2="768"/>
      <line x1="416" y1="768" x2="442" y2="785"/>
      <line x1="230" y1="880" x2="256" y2="897"/>
      <line x1="416" y1="897" x2="442" y2="880"/>
    </g>
    <g stroke="#d8e8b8" stroke-width="1">
      <line x1="779" y1="785" x2="805" y2="768"/>
      <line x1="965" y1="768" x2="991" y2="785"/>
      <line x1="779" y1="880" x2="805" y2="897"/>
      <line x1="965" y1="897" x2="991" y2="880"/>
    </g>
  </svg>

  <!-- back cover content -->
  <div class="back-brand">
    <p class="brand-name">MERIDIAN TRIALS INC.</p>
  </div>
  <div class="back-contact">
    <div class="contact-line">
      <svg viewBox="0 0 12 12" aria-label="Phone"><circle cx="6" cy="6" r="5.3" fill="none" stroke="#fff" stroke-width="1.2"/><path d="M4 3.5 L5 3.2 L5.6 4.6 L5 5.1 Q5.6 6.4 6.9 7 L7.4 6.4 L8.8 7 L8.5 8 Q6.8 8.4 5 6.9 Q3.5 5.3 4 3.5 Z" fill="#fff"/></svg>
      <span>+1-555-014-2290</span>
      <span class="gap"></span>
      <svg viewBox="0 0 12 12" aria-label="Email"><path d="M1 5 L6 1.5 L11 5 V10.5 H1 Z" fill="#fff"/><path d="M1.8 5.4 L6 8.2 L10.2 5.4" fill="none" stroke="#1a6aa0" stroke-width="0.9"/></svg>
      <span>hello@meridiantrials.net</span>
    </div>
    <div class="contact-line">Meridian Trials, Inc. 48 Birch Lane, Fairview, NY 10990</div>
  </div>

  <!-- front cover content -->
  <div class="front-brand">
    <div class="brand-mark"></div>
    <p class="brand-name">MERIDIAN TRIALS INC.</p>
  </div>
  <div class="front-web">www.<strong>meridiantrials</strong>.net</div>

  <!-- business cards in pockets -->
  <div class="card card-left">
    <div class="card-brand">
      <div class="brand-mark"></div>
      <p class="brand-name">MERIDIAN TRIALS INC.</p>
    </div>
    <div class="card-details">
      <div>
        <div>+1-555-014-2290</div>
        <div>hello@meridiantrials.net</div>
      </div>
      <div class="card-person">Your Name<br>Title</div>
    </div>
    <div class="card-address">Meridian Trials, Inc. 48 Birch Lane<br>Fairview, NY 10990</div>
  </div>

  <div class="card card-right">
    <div class="card-brand">
      <div class="brand-mark"></div>
      <p class="brand-name">MERIDIAN TRIALS INC.</p>
    </div>
    <div class="card-details">
      <div>
        <div>+1-555-014-2290</div>
        <div>hello@meridiantrials.net</div>
      </div>
      <div class="card-person">Your Name<br>Title</div>
    </div>
    <div class="card-address">Meridian Trials, Inc. 48 Birch Lane<br>Fairview, NY 10990</div>
  </div>
</div>
</body>
</html>
```